Artificial intelligence, machine learning, and automation company needs a sexy business card design

We need a sleek and sexy business card design for an AI consulting company based in Philadelphia PA. We provide custom machine learning and automation solutions for companies of all shapes and sizes. The primary industries that we serve are pharmaceuticals, engineering, healthcare, and computer software. We would like the designs to be a black business card that uses green as a sleek accent color. The final design should communicate intelligence, cutting edge new-tech, and optimization.

Target Market(s)

C-level and VP level executives of multi-million annual companies. Mostly in Pharma, Healthcare, Real Estate, Retail, and Engineering

Industry/Entity Type

Computer Software

Contact Information for Business Card

Name: Jack Moss
Title: CEO
Cell: 215 604 8293
Email: JackM@quillarcworks.example
Website: www.QuillarcWorks.example

Font styles to use
Sans Serif

Colors

Designer to choose colors to be used in the design.

Requirements
Must have
• 1) Attached Quillarc Logo (either with colors or not/embossed)
• 2) "Artificial Intelligence" "Automation" and "Machine Learning"
• 3) "Quillarc Laboratories" or "Quillarc Works" or "Quillarc"
• 4) Sexy AF.
Nice to have
• Black card / dark card color, "Quillarc Green" accent colors (in attached .ai file), Embossment of logo/name/etc, thick card stock, colored borders (on card sides, not front/back faces)
Should not have
• Should not be bland, or unsexy.

```html
<!DOCTYPE html>
<html lang="en">
<head>
<meta charset="utf-8">
<title>Quillarc Laboratories – Business Card</title>
<link rel="stylesheet" href="https://fonts.googleapis.com/css2?family=Raleway:wght@300;400;500;700&family=Open+Sans:wght@700&display=swap">
<style>
  :root {
    --backdrop: #e4e4e4;
    --card: #333333;
    --card-inset: #4a4a4a;
    --accent: #52c2aa;
    --ink: #ffffff;
  }
  * { margin: 0; padding: 0; box-sizing: border-box; }
  html, body { width: 1200px; height: 1000px; overflow: hidden; }
  body { position: relative; background: var(--backdrop); font-family: "Raleway", sans-serif; color: var(--ink); }

  .card { position: absolute; background: var(--card); }
  .card--front { left: 200px; top: 23px; width: 773px; height: 443px; }
  .card--back  { left: 200px; top: 506px; width: 775px; height: 442px; }

  /* Front: brand block */
  .brand-square {
    position: absolute; left: 282px; top: 80px; width: 218px; height: 207px;
    border: 7px solid var(--accent); background: var(--card-inset);
  }
  .brand-name {
    position: absolute; left: 0; width: 773px; top: 300px; text-align: center;
    font-weight: 400; color: var(--ink); line-height: 1;
  }
  .brand-name__main { display: block; font-size: 40px; letter-spacing: 5px; }
  .brand-name__sub { display: block; font-size: 18px; letter-spacing: 3.2px; margin-top: 12px; }

  /* Back: contact block */
  .contact { position: absolute; left: 448px; top: 54px; width: 310px; }
  .contact__name { font-size: 30px; font-weight: 300; letter-spacing: 0.5px; line-height: 1; }
  .contact__name strong { font-weight: 700; }
  .contact__title { margin: 20px 0 0 4px; font-size: 16px; font-weight: 700; color: var(--accent); letter-spacing: 0.5px; }
  .contact__rule { width: 163px; height: 3px; background: var(--accent); margin: 9px 0 0 4px; }
  .contact__list { list-style: none; margin: 24px 0 0 4px; }
  .contact__item { display: flex; align-items: baseline; height: 44px; white-space: nowrap; }
  .contact__label { font-size: 16px; font-weight: 300; color: var(--accent); letter-spacing: 0.3px; margin-right: 8px; }
  .contact__value { font-family: "Open Sans", sans-serif; font-weight: 700; font-size: 15px; }

  /* Back: small brand lockup */
  .lockup { position: absolute; left: 38px; top: 344px; display: flex; align-items: center; }
  .lockup__square { width: 66px; height: 63px; border: 3px solid var(--accent); }
  .lockup__name { margin-left: 14px; font-weight: 400; line-height: 1; color: var(--ink); }
  .lockup__main { display: block; font-size: 32px; letter-spacing: 3px; }
  .lockup__sub { display: block; font-size: 16px; letter-spacing: 2.8px; margin-top: 9px; }
</style>
</head>
<body>
  <section class="card card--front" aria-label="Card front">
    <div class="brand-square" aria-hidden="true"></div>
    <p class="brand-name">
      <span class="brand-name__main">QUILLARC</span>
      <span class="brand-name__sub">LABORATORIES</span>
    </p>
  </section>

  <section class="card card--back" aria-label="Card back">
    <div class="contact">
      <h1 class="contact__name">JACK <strong>MOSS</strong></h1>
      <p class="contact__title">CEO</p>
      <div class="contact__rule"></div>
      <ul class="contact__list">
        <li class="contact__item"><span class="contact__label">PHONE :</span><span class="contact__value">215 604 8293</span></li>
        <li class="contact__item"><span class="contact__label">EMAIL :</span><span class="contact__value">JackM@quillarcworks.example</span></li>
        <li class="contact__item"><span class="contact__label">WEBSITE:</span><span class="contact__value">www.QuillarcWorks.example</span></li>
      </ul>
    </div>
    <div class="lockup">
      <div class="lockup__square" aria-hidden="true"></div>
      <p class="lockup__name">
        <span class="lockup__main">QUILLARC</span>
        <span class="lockup__sub">LABORATORIES</span>
      </p>
    </div>
  </section>
</body>
</html>
```